Mandala Postcard Design

I am in need of a postcard to hand out at a Psychic Fair. I envision the card to having half-of-a Mandala (from my Facebook folder), touched up a bit to make it vibrant and bold. Others vendors will have cards w/photographic backgrounds doing yoga. I'd like mine to stand out for it's line-drawn "cartoonish" nature, solid-color nature. The wording would be my basic contact info and a short description ... something like: "Experience the Magic of Mandala Making ... Next Class will be held: (open space for writing, no lines) The art is contained in this Facebook folder. Lots to choose from, with my favorites being the stronger outlined designs.

https://www.sketchnook.example/Brightloom/media_set?set=a.20262926615637197.2184852941.783542196&type=3
Updates

I just uploaded a few new drawings that might work better, since they are more round. I want to minimize the white space, for instance, avoid having the left & right corners empty. Another idea could be to use 1/4 mandalas in the corners. I'm ready to make a decision. I want it to look great, but as I gain drawing experience, I'll need to update my cards. Thanks! I'm not sure if this the place for this comment, but I'll also be needing a DVD label for my tutorials, and a front page design for a mandala coloring book.

Target Market(s)

Primarily women interested in metaphysical, psychic, meditation, reiki and a basic interest in art.

Font styles to use
Serif
Sans Serif

Requirements
Should not have
• Should not be on a dark card, really should be a plain white background, it seems, in order to stand out.

```html
<!DOCTYPE html>
<html lang="en">
<head>
<meta charset="utf-8">
<title>Mandala Making Postcard</title>
<link rel="stylesheet" href="https://fonts.googleapis.com/css2?family=Sacramento&family=Open+Sans:wght@400&display=swap">
<style>
  :root {
    --paper: #ffffff;
    --ink: #1a1a1a;
    --pink: #f07c8e;
    --yellow: #fbf07a;
    --teal: #4fc3c9;
    --blue: #3aa6e0;
    --lime: #c9e04a;
    --red: #e53a3a;
  }
  html, body {
    margin: 0;
    padding: 0;
    overflow: hidden;
    background: var(--paper);
  }
  .postcard {
    position: relative;
    width: 1200px;
    height: 929px;
    overflow: hidden;
    background: var(--paper);
  }
  .mandala {
    position: absolute;
    border-radius: 50%;
  }
  .mandala--top-left {
    left: -85px; top: -40px;
    width: 290px; height: 290px;
    background: radial-gradient(circle, var(--yellow) 0%, var(--pink) 45%, var(--teal) 75%, rgba(255,255,255,0) 100%);
  }
  .mandala--feature {
    left: 22px; top: 210px;
    width: 524px; height: 524px;
    background: radial-gradient(circle, var(--pink) 0%, var(--yellow) 30%, var(--blue) 62%, var(--pink) 78%, var(--teal) 92%, rgba(79,195,201,0) 100%);
  }
  .mandala--top-right {
    left: 930px; top: -50px;
    width: 340px; height: 340px;
    background: radial-gradient(circle, var(--yellow) 0%, var(--pink) 40%, var(--teal) 70%, var(--red) 88%, rgba(255,255,255,0) 100%);
  }
  .mandala--bottom-left {
    left: -80px; top: 680px;
    width: 280px; height: 280px;
    background: radial-gradient(circle, var(--pink) 0%, var(--lime) 40%, var(--teal) 72%, rgba(255,255,255,0) 100%);
  }
  .mandala--bottom-right {
    left: 730px; top: 630px;
    width: 520px; height: 520px;
    background: radial-gradient(circle, var(--red) 0%, var(--yellow) 25%, var(--pink) 50%, var(--blue) 72%, var(--teal) 86%, rgba(255,255,255,0) 100%);
  }
  .headline {
    position: absolute;
    left: 566px; top: 300px;
    margin: 0;
    font-family: "Sacramento", cursive;
    font-weight: 400;
    font-size: 74px;
    line-height: 76px;
    color: var(--ink);
  }
  .next-class {
    position: absolute;
    left: 634px; top: 466px;
    margin: 0;
    font-family: "Open Sans", Arial, sans-serif;
    font-size: 20px;
    color: var(--ink);
  }
</style>
</head>
<body>
  <main class="postcard">
    <div class="mandala mandala--top-left" role="img" aria-label="Quarter mandala drawing in pink, yellow and teal"></div>
    <div class="mandala mandala--top-right" role="img" aria-label="Partial mandala drawing in pink, teal, yellow and red"></div>
    <div class="mandala mandala--feature" role="img" aria-label="Round mandala drawing with teal spiked rim, pink ring and yellow and blue segments"></div>
    <div class="mandala mandala--bottom-left" role="img" aria-label="Partial mandala drawing in pink, lime and teal"></div>
    <div class="mandala mandala--bottom-right" role="img" aria-label="Large petal mandala drawing in blue, pink, yellow and red"></div>

    <h1 class="headline">Experience the Magic of<br>Mandala Making</h1>
    <p class="next-class">Next Class will be held :</p>
  </main>
</body>
</html>
```